Cedarfield Supply METAL business card

A metal business card design. Attached are older designs for a reference, but we want a NEW design, not the same as in the past. See the 2 examples just posted. We would like some cut out in the design. Possibly the pine cone or the pine tree branch (see image IMG_0).

Target Market(s)

Home and Gardern

Industry/Entity Type

Landscape

Contact Information for Business Card

Logo, website, address, name, phone numbers

```html
<!DOCTYPE html>
<html lang="en">
<head>
<meta charset="utf-8">
<title>Cedarfield Supply – Metal Business Card</title>
<link rel="stylesheet" href="https://fonts.googleapis.com/css2?family=Arimo:wght@400;700&display=swap">
<style>
  :root {
    --page-bg: #e9e4dc;
    --card-black: #161616;
    --rust: #c8561f;
    --text-light: #ecebe8;
    --cutout-light: #d9d6d0;
    --cutout-warm: #b9ab95;
  }
  * { margin: 0; padding: 0; box-sizing: border-box; }
  html, body {
    width: 1200px;
    height: 900px;
    overflow: hidden;
    background: var(--page-bg);
    font-family: "Arimo", Arial, sans-serif;
  }
  .canvas {
    position: relative;
    width: 1200px;
    height: 900px;
  }
  .card {
    position: absolute;
    left: 270px;
    width: 660px;
    height: 380px;
    background: var(--card-black);
    border-radius: 0 34px 0 34px;
    box-shadow: 0 14px 30px rgba(0,0,0,0.28);
    overflow: hidden;
  }
  .card--front { top: 40px; }
  .card--back { top: 480px; }

  .cutout {
    position: absolute;
    border: 5px solid var(--rust);
    border-radius: 18px;
    background: linear-gradient(135deg, var(--cutout-light), var(--cutout-warm));
  }
  .card--front .cutout { left: 30px; top: 40px; width: 350px; height: 270px; }
  .card--back .cutout { left: 290px; top: 20px; width: 340px; height: 230px; }

  .brand {
    position: absolute;
    left: 410px;
    top: 160px;
    display: flex;
    align-items: center;
    gap: 12px;
  }
  .brand__mark {
    width: 22px;
    height: 22px;
    border-radius: 50%;
    background: var(--rust);
  }
  .brand__name {
    font-size: 26px;
    font-weight: 700;
    color: var(--rust);
  }

  .contact {
    position: absolute;
    left: 44px;
    bottom: 34px;
    color: var(--text-light);
    font-size: 17px;
    line-height: 1.35;
  }
  .contact__name {
    color: var(--rust);
    font-weight: 700;
    font-size: 22px;
    letter-spacing: 0.5px;
    text-transform: uppercase;
    margin-bottom: 12px;
  }
  .contact__address { margin-bottom: 12px; }
  .contact__row {
    display: flex;
    align-items: center;
    gap: 10px;
  }
  .contact__icon {
    width: 16px;
    height: 16px;
    flex: none;
  }
</style>
</head>
<body>
<div class="canvas">

  <section class="card card--front">
    <div class="cutout" role="img" aria-label="Cut-out map of the United States filled with pine needles and a pine cone"></div>
    <div class="brand">
      <span class="brand__mark"></span>
      <span class="brand__name">Cedarfield Supply</span>
    </div>
  </section>

  <section class="card card--back">
    <div class="cutout" role="img" aria-label="Cut-out map of the United States filled with pine needles and a pine cone"></div>
    <div class="contact">
      <p class="contact__name">Dale Morrow</p>
      <p class="contact__address">240 Quarry Bend Rd<br>Fairview, MS 39000, USA</p>
      <p class="contact__row">
        <svg class="contact__icon" viewBox="0 0 24 24" aria-hidden="true"><path fill="var(--rust)" d="M6.6 10.8a15.1 15.1 0 0 0 6.6 6.6l2.2-2.2a1 1 0 0 1 1-.25 11.4 11.4 0 0 0 3.6.57 1 1 0 0 1 1 1V20a1 1 0 0 1-1 1A17 17 0 0 1 3 4a1 1 0 0 1 1-1h3.5a1 1 0 0 1 1 1c0 1.25.2 2.45.57 3.57a1 1 0 0 1-.25 1z"/></svg>
        888-555-0142
      </p>
      <p class="contact__row">
        <svg class="contact__icon" viewBox="0 0 24 24" aria-hidden="true"><path fill="var(--rust)" d="M6.6 10.8a15.1 15.1 0 0 0 6.6 6.6l2.2-2.2a1 1 0 0 1 1-.25 11.4 11.4 0 0 0 3.6.57 1 1 0 0 1 1 1V20a1 1 0 0 1-1 1A17 17 0 0 1 3 4a1 1 0 0 1 1-1h3.5a1 1 0 0 1 1 1c0 1.25.2 2.45.57 3.57a1 1 0 0 1-.25 1z"/></svg>
        601-555-0187
      </p>
      <p class="contact__row">
        <svg class="contact__icon" viewBox="0 0 24 24" aria-hidden="true"><g fill="none" stroke="var(--rust)" stroke-width="2"><circle cx="12" cy="12" r="9"/><ellipse cx="12" cy="12" rx="4" ry="9"/><path d="M3 12h18M5 7h14M5 17h14"/></g></svg>
        cedarfieldsupply.com
      </p>
    </div>
  </section>

</div>
</body>
</html>
```